Brightvantage.com tech company website

Current site is www.brightvantage.com. The site will tell you about our company.

Designs we like are:
http://megainfo.quellorix.com
www.trelvo.com
www.morvasket.com

Target Market(s)

B2B

Industry/Entity Type

It Company

Coding

Coded - Design and coding required

Number of Pages Required

5+ page

Requirements
Must have
• We want to entice without giving away too much info. We like graphics and colors. But website must look official and credible.

```html
<!DOCTYPE html>
<html lang="en">
<head>
<meta charset="utf-8">
<title>Brightvantage</title>
<link rel="stylesheet" href="https://fonts.googleapis.com/css2?family=Open+Sans:ital,wght@0,400;0,600;0,700;1,600&display=swap">
<style>
  :root {
    --hero-deep: #040c16;
    --hero-mid: #0d2640;
    --hero-glow: #5d8cb3;
    --hero-horizon: #9cc4e2;
    --accent: #1d6fb8;
    --accent-light: #3a9be0;
    --heading: #1f3f66;
    --text: #555b62;
    --muted: #8a9096;
    --divider: #eceef0;
    --page: #ffffff;
    --footer: #2b2e31;
    --footer-line: #3a3e42;
    --footer-text: #a7abaf;
  }
  * { box-sizing: border-box; margin: 0; padding: 0; }
  html, body { width: 773px; height: 1200px; overflow: hidden; }
  body { font-family: "Open Sans", Arial, sans-serif; background: var(--page); color: var(--text); position: relative; }

  .hero {
    position: absolute; left: 0; top: 0; width: 773px; height: 455px; overflow: hidden;
    background:
      radial-gradient(ellipse 420px 70px at 50% 440px, rgba(156,196,226,.55), rgba(156,196,226,0) 70%),
      radial-gradient(circle 230px at 50% 250px, rgba(93,140,179,.75), rgba(13,38,64,0) 100%),
      radial-gradient(ellipse 300px 200px at 12% 30%, rgba(40,80,120,.35), rgba(4,12,22,0) 70%),
      radial-gradient(ellipse 300px 200px at 88% 70%, rgba(40,80,120,.3), rgba(4,12,22,0) 70%),
      linear-gradient(180deg, var(--hero-deep) 0%, var(--hero-mid) 55%, #1a3a5a 85%, var(--hero-deep) 100%);
  }
  .hero-art { position: absolute; inset: 0; }
  .hero-scan { position: absolute; left: 0; right: 0; top: 0; bottom: 0;
    background: repeating-linear-gradient(0deg, rgba(255,255,255,.025) 0 1px, transparent 1px 6px); }
  .site-header { position: absolute; left: 0; top: 0; width: 100%; height: 80px; z-index: 2; }
  .brand { position: absolute; left: 70px; top: 31px; display: flex; align-items: center; gap: 8px; }
  .brand-dot { width: 14px; height: 14px; border-radius: 50%; background: var(--accent-light); }
  .brand-name { color: #fff; font-size: 18px; font-weight: 600; letter-spacing: .5px; }
  .main-nav { position: absolute; right: 66px; top: 40px; display: flex; gap: 18px; }
  .main-nav a { color: #fff; font-size: 8.5px; font-weight: 600; text-decoration: none; text-transform: uppercase; letter-spacing: .4px; }
  .lang { position: absolute; right: 40px; top: 8px; background: #fff; color: #333; font-size: 7px; padding: 2px 6px; border-radius: 2px; }

  .hero-kicker { position: absolute; top: 228px; width: 100%; text-align: center; color: #dbe6f0; font-size: 11px; letter-spacing: 1.5px; font-weight: 600; z-index: 2; }
  .hero-title { position: absolute; top: 248px; width: 100%; text-align: center; color: #fff; font-size: 30px; font-weight: 700; letter-spacing: 4px; z-index: 2; }
  .slide-arrow { position: absolute; top: 195px; width: 22px; height: 22px; background: rgba(255,255,255,.22); z-index: 2; display: flex; align-items: center; justify-content: center; }
  .slide-arrow.prev { left: 10px; } .slide-arrow.next { right: 10px; }

  .btn { display: inline-block; background: linear-gradient(var(--accent-light), var(--accent)); color: #fff; font-size: 9px; font-weight: 700;
    letter-spacing: 1px; padding: 7px 22px; border-radius: 14px; text-transform: uppercase; text-decoration: none; }
  .hero .btn { position: absolute; left: 324px; top: 320px; z-index: 2; }

  .welcome { position: absolute; top: 455px; left: 0; width: 100%; height: 235px; text-align: center; }
  .welcome h2 { margin-top: 16px; color: #333; font-size: 17px; font-weight: 600; letter-spacing: 1.5px; }
  .welcome h3 { margin-top: 16px; color: var(--accent); font-size: 17px; font-style: italic; font-weight: 600; }
  .welcome p { width: 520px; margin: 12px auto 0; font-size: 8px; line-height: 1.6; color: var(--text); }
  .welcome .btn { margin-top: 18px; }

  .features { position: absolute; top: 690px; left: 0; width: 100%; height: 365px;
    background: linear-gradient(180deg, var(--divider) 0, var(--divider) 26px, var(--page) 26px); border-top: 1px solid #dfe2e5; }

  .service { position: absolute; top: 720px; width: 310px; text-align: center; }
  .service.left { left: 66px; } .service.right { left: 398px; }
  .service-image { height: 170px; border: 4px solid #fff; box-shadow: 0 1px 4px rgba(0,0,0,.3); }
  .service.left .service-image {
    background:
      radial-gradient(ellipse 90px 80px at 58% 65%, rgba(255,255,255,.75), rgba(255,255,255,0) 70%),
      radial-gradient(ellipse 140px 60px at 30% 35%, rgba(255,255,255,.45), rgba(255,255,255,0) 70%),
      linear-gradient(135deg, #e3f2fb 0%, #8cc6ea 35%, #3d8fcf 70%, #1b5a94 100%);
  }
  .service.right .service-image {
    background:
      radial-gradient(ellipse 60px 70px at 78% 60%, rgba(60,66,74,.35), rgba(60,66,74,0) 70%),
      radial-gradient(ellipse 110px 40px at 35% 58%, rgba(255,255,255,.9), rgba(255,255,255,0) 70%),
      linear-gradient(180deg, #f4f5f6 0%, #e2e4e6 55%, #b9bdc1 100%);
  }
  .service h4 { margin-top: 17px; color: var(--heading); font-size: 13px; font-weight: 700; letter-spacing: .5px; text-transform: uppercase; }
  .service p { margin: 8px auto 0; width: 280px; font-size: 7.5px; line-height: 1.6; }
  .service .btn { margin-top: 12px; padding: 6px 18px; font-size: 8px; text-transform: none; letter-spacing: 0; }

  .site-footer { position: absolute; top: 1055px; left: 0; width: 100%; height: 145px; background: var(--footer); }
  .social { position: absolute; top: 22px; width: 100%; display: flex; justify-content: center; gap: 12px; }
  .social span { width: 20px; height: 20px; border-radius: 50%; background: #45494d; border: 1.5px solid #6d7276;
    box-shadow: inset 0 0 0 4px #45494d, inset 0 0 0 9px #8d9296; }
  .offices { position: absolute; top: 74px; width: 100%; display: flex; justify-content: center; gap: 110px; border-top: 1px solid var(--footer-line); padding-top: 8px; }
  .offices span { color: var(--footer-text); font-size: 7.5px; }
  .copyright { position: absolute; bottom: 20px; width: 100%; text-align: center; color: var(--muted); font-size: 7px; }
  .copyright b { color: var(--accent-light); font-weight: 400; }
</style>
</head>
<body>
  <section class="hero">
    <div class="hero-art" role="img" aria-label="Businessman standing before a glowing digital globe with data streams"></div>
    <div class="hero-scan"></div>
    <header class="site-header">
      <div class="brand"><span class="brand-dot"></span><span class="brand-name">Brightvantage</span></div>
      <nav class="main-nav">
        <a href="#">Home</a><a href="#">About</a><a href="#">Big Data and Analytics</a>
        <a href="#">Perception and Influence</a><a href="#">Case Studies</a>
      </nav>
      <span class="lang">English</span>
    </header>
    <span class="slide-arrow prev"><svg width="8" height="10" viewBox="0 0 8 10"><path d="M6 1 2 5l4 4" fill="none" stroke="#fff" stroke-width="1.6"/></svg></span>
    <span class="slide-arrow next"><svg width="8" height="10" viewBox="0 0 8 10"><path d="M2 1l4 4-4 4" fill="none" stroke="#fff" stroke-width="1.6"/></svg></span>
    <p class="hero-kicker">VOLUPTAS SIT ASPERNATUR</p>
    <h1 class="hero-title">STARTS WITH YOU</h1>
    <a class="btn" href="#">Learn More</a>
  </section>

  <section class="welcome">
    <h2>WELCOME</h2>
    <h3>Brightvantage is a privately held company</h3>
    <p>Brightvantage is a privately held company with offices in 4 states, and a backbone of over 100 technical staff dedicated to delivering desired outcomes of all types to businesses and high net worth individuals. Brightvantage has two core competencies: Big Data and Analytics and Perception and Influence Activities.</p>
    <a class="btn" href="#">Learn More</a>
  </section>

  <div class="features"></div>

  <article class="service left">
    <div class="service-image" role="img" aria-label="Woman touching a transparent screen of data charts"></div>
    <h4>Big Data and Analytics</h4>
    <p>Brightvantage is expert at data collection and analysis, extracting the data important to business, and putting it into a format that is useful.</p>
    <a class="btn" href="#">Learn More</a>
  </article>

  <article class="service right">
    <div class="service-image" role="img" aria-label="Businessman standing apart from a row of white figures"></div>
    <h4>Perception and Influence Activities</h4>
    <p>We proactively manage the internet, we make things trend, we make people think and feel what you want them to.</p>
    <a class="btn" href="#">Learn More</a>
  </article>

  <footer class="site-footer">
    <div class="social" aria-label="Social links"><span></span><span></span><span></span><span></span><span></span></div>
    <div class="offices"><span>Fort Lauderdale</span><span>Washington DC</span><span>New York City</span><span>Las Vegas</span></div>
    <p class="copyright"><b>Brightvantage</b> © 2016 | Privacy Policy</p>
  </footer>
</body>
</html>
```